Family business needs stationery redesign with new logo

Family owned company, established in 1987 wanting a brand 'refresh'. We are an electrical, refrigeration and construction company based in the Barkly Region Northern Territory, Australia. We have a new logo we would like to use which is uploaded along with our current letterhead and email signature. We are also dropping the word 'contractors' so please do not include this on any designs. Please note also, the 'orange' color used in our logo and designs should be Northern Territory red ochre which is as follows:

RGB (Hex): #C75B12
PantoneĀ® 159 C
CMYK: 1 / 74 / 100 / 7

We are needing our stationery redesigned using our new logo. Please include letterheads, business cards, envelopes, and email signatures.

We currently use our business letterheads for quotations, invoices, letters, HR matters, and internal memos.

We also need a separate simplified letterhead for internal paperwork such as employee leave forms, meeting agendas, and meeting minutes etc.
Updates

Reason: Needing more submissions of full package designs. We are wanting all our stationery, including business cards, letterheads, email signatures, envelopes, etc to be cohesive. We also require ALL the information, as supplied on our template letterhead, to be included on the new letterhead designs. including electrical license no.etc Thank you, R&K

Reason: needing more time as work has got in the way of looking over designs. A lot of designs not meeting the brief/criteria.

Industry/Entity Type

Business

Colors
0355a3
f37122

Requirements
Must have
• The 'orange' color used in the designs should be Northern Territory red ochre which is as follows:
• RGB (Hex): #C75B12
• PantoneĀ® 159 C
• CMYK: 1 / 74 / 100 / 7
• ***MUST INCLUDE ALL INFORMATION THAT IS ON OUR CURRENT LETTERHEAD***
Should not have
• Please do not include the word 'contractors'

```html
<!DOCTYPE html>
<html lang="en">
<head>
<meta charset="utf-8">
<title>R&amp;K Stationery Set</title>
<link rel="stylesheet" href="https://fonts.googleapis.com/css2?family=Open+Sans:wght@400;600;700&display=swap">
<style>
  :root {
    --navy: #22336b;
    --ochre: #c75b12;
    --paper: #ffffff;
    --backdrop: #ebe8e3;
    --tint: #e4e5ef;
    --ink-soft: #3a3f5c;
  }
  * { box-sizing: border-box; margin: 0; padding: 0; }
  html, body { width: 1200px; height: 1200px; overflow: hidden; }
  body {
    background: var(--backdrop);
    font-family: "Open Sans", sans-serif;
    position: relative;
  }
  .sheet {
    position: absolute;
    background: var(--paper);
    overflow: hidden;
    box-shadow: 0 2px 8px rgba(0,0,0,0.18);
  }
  .wordmark {
    font-family: "Open Sans", sans-serif;
    font-weight: 700;
    color: var(--navy);
    line-height: 1;
    letter-spacing: 1px;
  }
  .abn { color: var(--ochre); font-weight: 400; }

  /* Soft decorative tint area */
  .tint-area {
    position: absolute;
    background: radial-gradient(ellipse at center, var(--tint) 0%, rgba(228,229,239,0.6) 55%, rgba(228,229,239,0) 75%);
  }

  /* Letterhead */
  .letterhead { left: 50px; top: 50px; width: 600px; height: 849px; }
  .letterhead .brand { position: absolute; left: 48px; top: 60px; }
  .letterhead .wordmark { font-size: 60px; }
  .letterhead .abn { font-size: 15px; margin-top: 12px; padding-left: 50px; }
  .letterhead .intro {
    position: absolute; right: 40px; top: 40px; width: 250px;
    font-size: 11.5px; line-height: 1.4; color: var(--navy); text-align: justify;
  }
  .letterhead .tint-area { left: 300px; top: 560px; width: 420px; height: 340px; }
  .letterhead .edge { position: absolute; left: 0; bottom: 0; width: 100%; height: 4px; background: var(--navy); }

  /* Envelope */
  .envelope { left: 690px; top: 50px; width: 460px; height: 268px; }
  .envelope .flap {
    position: absolute; left: 0; top: 0; width: 100%; height: 65px;
    background: var(--ochre); border-radius: 12px 12px 0 0;
    display: flex; align-items: center; justify-content: center;
  }
  .envelope .flap .wordmark { color: #fff; font-size: 30px; }
  .envelope .note {
    position: absolute; left: 16px; top: 222px; width: 126px;
    font-size: 6px; line-height: 1.4; color: var(--navy); text-align: justify;
  }
  .envelope .tint-area { left: 250px; top: 110px; width: 260px; height: 200px; }

  /* Business card front */
  .card-front { left: 690px; top: 370px; width: 460px; height: 262px; }
  .card-front .brand { position: absolute; left: 40px; top: 22px; }
  .card-front .wordmark { font-size: 34px; }
  .card-front .abn { font-size: 12px; margin-top: 8px; padding-left: 30px; }
  .card-front .person { position: absolute; left: 52px; top: 114px; display: flex; align-items: center; }
  .card-front .name { color: var(--ochre); font-size: 19px; font-weight: 400; }
  .card-front .role {
    border-left: 1px solid #bbb; margin-left: 8px; padding-left: 8px;
    font-size: 6.5px; font-weight: 700; color: var(--navy); letter-spacing: 0.3px;
  }
  .card-front .contact { position: absolute; left: 50px; top: 160px; font-size: 9.5px; line-height: 1.5; color: var(--ink-soft); }
  .card-front .contact dt { color: var(--ochre); display: inline; }
  .card-front .contact dd { display: inline; }
  .card-front .contact .line { display: block; }
  .card-front .contact .gap { margin-top: 6px; }
  .card-front .contact .indent { padding-left: 42px; }
  .card-front .tint-area { left: 330px; top: -10px; width: 150px; height: 282px; }

  /* Business card back */
  .card-back {
    left: 690px; top: 672px; width: 460px; height: 262px; background: var(--navy);
    display: flex; flex-direction: column; align-items: center; justify-content: center;
  }
  .card-back .wordmark { color: #fff; font-size: 44px; }
  .card-back .abn { color: #fff; font-size: 16px; margin-top: 14px; }
</style>
</head>
<body>

  <section class="sheet letterhead" aria-label="Letterhead">
    <div class="tint-area" role="img" aria-label="Faint brand decoration area"></div>
    <header class="brand">
      <div class="wordmark">R&amp;K</div>
      <div class="abn">ABN 12</div>
    </header>
    <p class="intro">Lorem Ipsum is simply dummy text of the printing and typesetting industry. Lorem Ipsum has been the industry's standard dummy text ever since the 1500.</p>
    <div class="edge"></div>
  </section>

  <section class="sheet envelope" aria-label="Envelope">
    <div class="tint-area" role="img" aria-label="Faint brand decoration area"></div>
    <div class="flap"><span class="wordmark">R&amp;K</span></div>
    <p class="note">Lorem Ipsum is simply dummy text of the printing and typesetting industry. Lorem Ipsum has been the industry's standard dummy text ever since the 1500.</p>
  </section>

  <section class="sheet card-front" aria-label="Business card front">
    <div class="tint-area" role="img" aria-label="Faint brand decoration area"></div>
    <header class="brand">
      <div class="wordmark">R&amp;K</div>
      <div class="abn">ABN 12</div>
    </header>
    <div class="person">
      <span class="name">DANA</span>
      <span class="role">CORPORATE SERVICES MANAGER</span>
    </div>
    <dl class="contact">
      <span class="line"><dt>Address: </dt><dd>PO Box 2040, 52 Ridge St,</dd></span>
      <span class="line indent">Alder Creek NT 0870</span>
      <span class="line"><dt>Ph: </dt><dd>08 5550&nbsp;&nbsp; </dd><dt>Cell: </dt><dd>0400</dd></span>
      <span class="line gap"><dt>Email: </dt><dd>@rkservices.com.au</dd></span>
      <span class="line gap"><dt>Web: </dt><dd>www.rkservices.com.au</dd></span>
    </dl>
  </section>

  <section class="sheet card-back" aria-label="Business card back">
    <div class="wordmark">R&amp;K</div>
    <div class="abn">ABN 12</div>
  </section>

</body>
</html>
```